Luxury Caviar Tin Label for High End Caviar Retailer

We are looking for a new caviar label design. We want something unique, preferably black and gold or dark blue and gold. We want a modern and luxurious feel. We have several types of caviar so we need to be able to change the name of the caviar when we print the labels. See inspiration attached. Logo is also attached. More about us: kvmarlune.com

Industry/Entity Type

fine foods industry, caviar

Font styles to use
Serif
Decorative

Requirements
Must have
• KV Marlune Logo, space for caviar name
Nice to have
• black and gold, blue and gold

```html
<!DOCTYPE html>
<html lang="en">
<head>
<meta charset="utf-8">
<title>KV Marlune Caviar Tin Label</title>
<link rel="stylesheet" href="https://fonts.googleapis.com/css2?family=Marcellus&display=swap">
<style>
  :root {
    --page: #ffffff;
    --tin-black: #000000;
    --gold: #9c7a2c;
    --gold-light: #b8953f;
    --gold-deep: #6e561c;
    --ink: #111111;
  }
  html, body {
    margin: 0;
    padding: 0;
    overflow: hidden;
    background: var(--page);
  }
  .sheet {
    position: relative;
    width: 1200px;
    height: 1000px;
    overflow: hidden;
    background: var(--page);
    font-family: "Marcellus", Georgia, serif;
  }
  .sheet-note {
    position: absolute;
    left: 744px;
    top: 46px;
    width: 400px;
    margin: 0;
    text-align: center;
    font-size: 29px;
    line-height: 1.2;
    font-weight: 400;
    color: var(--ink);
  }
  .label {
    position: absolute;
    display: block;
  }
  .label--main { left: 116px; top: 56px; width: 476px; height: 476px; }
  .label--variant { left: 786px; top: 158px; width: 328px; height: 328px; }
  .label--blank { left: 786px; top: 584px; width: 328px; height: 328px; }
  .label text {
    font-family: "Marcellus", Georgia, serif;
    fill: var(--gold);
  }
</style>
</head>
<body>
<main class="sheet">
  <h1 class="sheet-note">Changeable<br>Vector Files + psd</h1>

  <svg width="0" height="0" style="position:absolute" aria-hidden="true">
    <defs>
      <linearGradient id="crest-tone" x1="0" y1="0" x2="0" y2="1">
        <stop offset="0" stop-color="#8a6a24"/>
        <stop offset="1" stop-color="#5c4616"/>
      </linearGradient>
      <path id="caviar-arc" d="M -210 0 A 210 210 0 0 1 210 0"/>
      <symbol id="label-base" viewBox="-300 -300 600 600">
        <circle class="tin-face" r="298" fill="var(--tin-black)"/>
        <circle class="outer-ring" r="255" fill="none" stroke="var(--gold)" stroke-width="4"/>
        <path class="inner-arch" d="M -157 70 A 172 172 0 1 1 157 70" fill="none" stroke="var(--gold)" stroke-width="4"/>
        <text class="word-caviar" font-size="84" letter-spacing="22" fill="var(--gold)" font-family="Marcellus, Georgia, serif">
          <textPath href="#caviar-arc" startOffset="50%" text-anchor="middle">CAVIAR</textPath>
        </text>
        <g class="dot-cluster" fill="var(--gold-light)">
          <circle cx="-236" cy="-40" r="7"/><circle cx="-236" cy="-6" r="7"/><circle cx="-236" cy="28" r="7"/>
          <circle cx="-216" cy="-24" r="8"/><circle cx="-216" cy="12" r="8"/><circle cx="-216" cy="46" r="8"/>
          <circle cx="-192" cy="-40" r="8"/><circle cx="-192" cy="-6" r="8"/><circle cx="-192" cy="28" r="8"/>
          <circle cx="236" cy="-40" r="7"/><circle cx="236" cy="-6" r="7"/><circle cx="236" cy="28" r="7"/>
          <circle cx="216" cy="-24" r="8"/><circle cx="216" cy="12" r="8"/><circle cx="216" cy="46" r="8"/>
          <circle cx="192" cy="-40" r="8"/><circle cx="192" cy="-6" r="8"/><circle cx="192" cy="28" r="8"/>
          <circle cx="-179" cy="150" r="7"/><circle cx="-148" cy="150" r="7"/><circle cx="-116" cy="150" r="7"/>
          <circle cx="116" cy="150" r="7"/><circle cx="148" cy="150" r="7"/><circle cx="179" cy="150" r="7"/>
        </g>
        <rect class="crest-area" role="img" aria-label="Heraldic crest with rampant lion and scrollwork" x="-165" y="-112" width="330" height="170" rx="40" fill="url(#crest-tone)"/>
        <rect class="name-banner" x="-197" y="70" width="395" height="55" fill="none" stroke="var(--gold)" stroke-width="3"/>
        <rect class="flourish flourish--upper" role="img" aria-label="Gold scroll flourish" x="-88" y="141" width="176" height="16" rx="8" fill="var(--gold-deep)"/>
        <rect class="flourish flourish--lower" role="img" aria-label="Gold scroll flourish" x="-76" y="212" width="152" height="16" rx="8" fill="var(--gold-deep)"/>
      </symbol>
    </defs>
  </svg>

  <svg class="label label--main" viewBox="-300 -300 600 600" role="group" aria-label="Osetra Gold label">
    <use href="#label-base" x="-300" y="-300" width="600" height="600"/>
    <text class="brand-name" x="0" y="112" font-size="42" text-anchor="middle">KV MARLUNE</text>
    <text class="caviar-name" x="0" y="198" font-size="36" text-anchor="middle">OSETRA GOLD</text>
  </svg>

  <svg class="label label--variant" viewBox="-300 -300 600 600" role="group" aria-label="Label with changeable caviar name">
    <use href="#label-base" x="-300" y="-300" width="600" height="600"/>
    <text class="brand-name" x="0" y="112" font-size="42" text-anchor="middle">KV MARLUNE</text>
    <text class="caviar-name" x="0" y="194" font-size="30" text-anchor="middle">SEVERAL NAMES</text>
  </svg>

  <svg class="label label--blank" viewBox="-300 -300 600 600" role="group" aria-label="Label with empty caviar name space">
    <use href="#label-base" x="-300" y="-300" width="600" height="600"/>
    <text class="brand-name" x="0" y="112" font-size="42" text-anchor="middle">KV MARLUNE</text>
  </svg>
</main>
</body>
</html>
```